New Website for Manufacturing Company - PSD only, no coding - CLOSED TO NEW DESIGNERS

IF YOU HAVE NOT ALREADY SUBMITTED A DESIGN PLEASE DO NOT SUBMIT ONE.
This is a re-work of an existing website. We can keep the themes and color schemes the same but we will be changing the layout and page content.
The scope includes the creation of some icons/sketches that will form some of the page content.
The scope is design only, no coding.
There are four files that have been uploaded that give a more detailed project brief, please read them.
Target Market(s)
Manufacturing
Industry/Entity Type
It Company
Number of Pages Required
1 page
Look and feel
Each slider illustrates characteristics of the customer's brand and the style your logo design should communicate.

```html
<!DOCTYPE html>
<html lang="en">
<head>
<meta charset="utf-8">
<title>Kestrel Manufacturing – Capabilities</title>
<link href="https://fonts.googleapis.com/css2?family=Open+Sans:wght@400;600;700;800&display=swap" rel="stylesheet">
<style>
  :root{
    --navy:#0e2a4c;
    --navy-deep:#0a1f38;
    --blue:#1f5fa6;
    --ink:#2d3540;
    --muted:#8a929c;
    --line:#e3e6ea;
    --icon-bg:#e9edf2;
    --white:#ffffff;
  }
  *{box-sizing:border-box;margin:0;padding:0}
  html,body{width:710px;height:1200px;overflow:hidden}
  body{font-family:"Open Sans",Arial,sans-serif;color:var(--ink);background:var(--white);position:relative}

  .site-header{height:84px;position:relative}
  .brand{position:absolute;left:30px;top:28px;font-weight:700;font-size:22px;color:var(--navy);letter-spacing:.3px;display:flex;align-items:center;gap:8px}
  .brand-mark{width:14px;height:14px;background:var(--blue)}
  .call-box{position:absolute;right:30px;top:14px;text-align:right}
  .call-box .ask{font-size:9px;color:var(--blue);font-weight:600}
  .call-box .today{font-size:8px;color:var(--muted)}
  .call-box .phone{font-size:20px;font-weight:700;color:var(--navy);display:flex;align-items:center;gap:6px;justify-content:flex-end}

  .main-nav{height:22px;display:flex;gap:26px;padding-left:30px;align-items:center}
  .main-nav a{font-size:9px;font-weight:700;color:var(--navy);text-decoration:none;letter-spacing:.4px}
  .main-nav a.active{color:var(--blue)}

  .hero{position:absolute;left:0;top:108px;width:710px;height:210px;background:var(--navy);overflow:hidden}
  .hero-art{position:absolute;inset:0;background:
      radial-gradient(ellipse 180px 70px at 140px 150px,rgba(200,220,245,.16),transparent 70%),
      radial-gradient(ellipse 150px 70px at 360px 155px,rgba(200,220,245,.14),transparent 70%),
      radial-gradient(ellipse 170px 70px at 580px 150px,rgba(200,220,245,.16),transparent 70%),
      linear-gradient(180deg,#0e2a4c 0%,#183a63 100%)}
  .hero-title{position:absolute;left:0;right:0;top:14px;text-align:center;color:var(--white);font-size:22px;font-weight:600;letter-spacing:.5px}
  .hero-title .quote{font-size:34px;font-weight:800;color:#9fc3ea;vertical-align:-10px;margin:0 6px}
  .hero-sub{position:absolute;left:0;right:0;top:50px;text-align:center;color:#c9d7e8;font-size:10px}

  .capabilities{position:absolute;top:334px;left:0;width:710px;text-align:center}
  .section-title{font-size:17px;font-weight:700;color:var(--blue);letter-spacing:.5px}
  .section-rule{width:60px;height:2px;background:var(--blue);margin:6px auto 10px}
  .tagline{font-size:11px;font-weight:700;color:var(--ink)}
  .intro{font-size:8px;color:var(--muted);margin-top:3px}

  .cap-grid{position:absolute;top:440px;left:55px;width:600px;display:grid;grid-template-columns:repeat(3,200px);row-gap:24px}
  .cap-item{height:168px;display:flex;flex-direction:column;align-items:center}
  .cap-icon{flex:0 0 78px;width:78px;height:78px;border-radius:50%;background:radial-gradient(circle at 50% 55%,#cfdcec,var(--icon-bg) 70%)}
  .cap-icon.blank{background:var(--icon-bg)}
  .cap-body{width:104px;margin-top:12px;text-align:left}
  .cap-name{font-size:13px;font-weight:700;color:var(--blue);text-align:center;white-space:nowrap;margin:0 -40px}
  .cap-list{list-style:none;margin-top:4px}
  .cap-list li{font-size:7.5px;color:var(--muted);line-height:11px}
  .cap-list li::before{content:"• "}
  .read-more{display:block;margin-top:6px;font-size:7.5px;font-weight:700;color:var(--navy);text-decoration:none}

  .site-footer{position:absolute;left:0;top:1022px;width:710px;height:150px;background:var(--navy);padding:20px 30px 0}
  .footer-cols{display:flex}
  .footer-col{width:107px}
  .footer-col.wide{width:112px}
  .footer-col h4{font-size:8px;font-weight:700;color:var(--white);letter-spacing:.4px;margin-bottom:6px}
  .footer-col li{list-style:none;font-size:7px;color:#aab8c9;line-height:12px}
  .social{display:flex;gap:6px;margin-top:6px}
  .social span{width:12px;height:12px;border-radius:50%;background:#3a5a80}
  .footer-bar{position:absolute;left:0;top:1172px;width:710px;height:28px;background:var(--navy-deep);border-top:3px solid var(--blue);display:flex;align-items:center;gap:24px;padding-left:30px}
  .footer-bar p{font-size:7px;color:#8fa2b8}
</style>
</head>
<body>

<header class="site-header">
  <div class="brand"><span class="brand-mark"></span>Kestrel Manufacturing</div>
  <div class="call-box">
    <div class="ask">Have a Question?</div>
    <div class="today">Call Today</div>
    <div class="phone">
      <svg width="14" height="14" viewBox="0 0 24 24" aria-hidden="true"><path fill="#1f5fa6" d="M6.6 10.8a15 15 0 0 0 6.6 6.6l2.2-2.2a1 1 0 0 1 1-.25 11.4 11.4 0 0 0 3.6.57 1 1 0 0 1 1 1V20a1 1 0 0 1-1 1A17 17 0 0 1 3 4a1 1 0 0 1 1-1h3.5a1 1 0 0 1 1 1c0 1.25.2 2.45.57 3.57a1 1 0 0 1-.25 1z"/></svg>
      555 014 2200
    </div>
  </div>
</header>

<nav class="main-nav">
  <a href="#">HOME</a>
  <a href="#" class="active">CAPABILITIES</a>
  <a href="#">SERVICES</a>
  <a href="#">MARKETS</a>
  <a href="#">MATERIALS</a>
  <a href="#">DOCUMENTATION</a>
  <a href="#">CONTACT US</a>
</nav>

<section class="hero">
  <div class="hero-art" role="img" aria-label="White line sketches of machined and formed insulation parts on a navy background"></div>
  <h1 class="hero-title"><span class="quote">“</span>HIGH TEMPERATURE INSULATION EXPERTS<span class="quote">”</span></h1>
  <p class="hero-sub">We Manufacture, Fabricate and Distribute high temperature insulating materials.</p>
</section>

<section class="capabilities">
  <h2 class="section-title">OUR CAPABILITIES</h2>
  <div class="section-rule"></div>
  <p class="tagline">We are Manufacture. We are fabricate what you need. We distribute to where you need it.</p>
  <p class="intro">Precision insulation parts cut, formed and shipped to your specifications every day.</p>
</section>

<div class="cap-grid">
  <article class="cap-item">
    <div class="cap-icon" role="img" aria-label="Water jet cutting head illustration"></div>
    <div class="cap-body"><h3 class="cap-name">Water Jet</h3>
      <ul class="cap-list"><li>Precision cut parts</li><li>Tight tolerances</li><li>Fast turnaround</li></ul>
      <a class="read-more" href="#">READ MORE ›</a></div>
  </article>
  <article class="cap-item">
    <div class="cap-icon" role="img" aria-label="Casting mould illustration"></div>
    <div class="cap-body"><h3 class="cap-name">Casting</h3>
      <ul class="cap-list"><li>Precision cut parts</li><li>Tight tolerances</li><li>Fast turnaround</li></ul>
      <a class="read-more" href="#">READ MORE ›</a></div>
  </article>
  <article class="cap-item">
    <div class="cap-icon" role="img" aria-label="Laminating layers illustration"></div>
    <div class="cap-body"><h3 class="cap-name">Laminating</h3>
      <ul class="cap-list"><li>Precision cut parts</li><li>Tight tolerances</li><li>Fast turnaround</li></ul>
      <a class="read-more" href="#">READ MORE ›</a></div>
  </article>
  <article class="cap-item">
    <div class="cap-icon" role="img" aria-label="Slitting roll illustration"></div>
    <div class="cap-body"><h3 class="cap-name">Slitting</h3>
      <ul class="cap-list"><li>Precision cut parts</li><li>Tight tolerances</li><li>Fast turnaround</li></ul>
      <a class="read-more" href="#">READ MORE ›</a></div>
  </article>
  <article class="cap-item">
    <div class="cap-icon" role="img" aria-label="CNC machining illustration"></div>
    <div class="cap-body"><h3 class="cap-name">CNC Machining</h3>
      <ul class="cap-list"><li>Precision cut parts</li><li>Tight tolerances</li><li>Fast turnaround</li></ul>
      <a class="read-more" href="#">READ MORE ›</a></div>
  </article>
  <article class="cap-item">
    <div class="cap-icon" role="img" aria-label="Die cutting sheet illustration"></div>
    <div class="cap-body"><h3 class="cap-name">Die Cutting</h3>
      <ul class="cap-list"><li>Precision cut parts</li><li>Tight tolerances</li><li>Fast turnaround</li></ul>
      <a class="read-more" href="#">READ MORE ›</a></div>
  </article>
  <article class="cap-item">
    <div class="cap-icon" role="img" aria-label="Vacuum forming illustration"></div>
    <div class="cap-body"><h3 class="cap-name">Vacuum Forming</h3>
      <ul class="cap-list"><li>Precision cut parts</li><li>Tight tolerances</li><li>Fast turnaround</li></ul>
      <a class="read-more" href="#">READ MORE ›</a></div>
  </article>
  <article class="cap-item">
    <div class="cap-icon blank" role="img" aria-label="Placeholder for a capability illustration"></div>
    <div class="cap-body"><h3 class="cap-name">Another</h3>
      <ul class="cap-list"><li>Precision cut parts</li><li>Tight tolerances</li><li>Fast turnaround</li></ul>
      <a class="read-more" href="#">READ MORE ›</a></div>
  </article>
  <article class="cap-item">
    <div class="cap-icon blank" role="img" aria-label="Placeholder for a capability illustration"></div>
    <div class="cap-body"><h3 class="cap-name">Another</h3>
      <ul class="cap-list"><li>Precision cut parts</li><li>Tight tolerances</li><li>Fast turnaround</li></ul>
      <a class="read-more" href="#">READ MORE ›</a></div>
  </article>
</div>

<footer class="site-footer">
  <div class="footer-cols">
    <div class="footer-col"><h4>CAPABILITIES</h4><ul><li>Casting</li><li>Vacuum Forming</li><li>Slitting</li><li>Waterjet cutting</li><li>CNC machining</li><li>Die cutting</li></ul></div>
    <div class="footer-col"><h4>SERVICES</h4><ul><li>Design</li><li>Rapid prototyping</li><li>Stocking</li><li>Kitting</li><li>Assembly</li></ul></div>
    <div class="footer-col"><h4>MARKETS</h4><ul><li>Appliance</li><li>HVAC</li><li>Glass</li><li>Industrial</li></ul></div>
    <div class="footer-col"><h4>MATERIALS</h4><ul><li>Fiber Paper</li><li>Microporous</li><li>Ceramic Fiber</li><li>Cast Board</li><li>Mineral Wool</li><li>Fiberglass</li></ul></div>
    <div class="footer-col wide"><h4>DOCUMENTATION</h4><ul><li>Data Sheets</li><li>Safety Sheets</li><li>Terms &amp; Conditions</li></ul></div>
    <div class="footer-col wide"><h4>CONTACT US</h4><ul><li>sales@kestrelmfg.example</li><li>PH: 555 014 2200</li><li>FAX: 555 014 2201</li><li>12 Harbor Street, Milford, MA 01000</li></ul>
      <div class="social"><span></span><span></span><span></span></div></div>
  </div>
</footer>
<div class="footer-bar">
  <p>© Kestrel Manufacturing 2017</p>
  <p>Terms &amp; Conditions | Privacy Policy</p>
</div>

</body>
</html>
```